Book cover for a very impressive real-life healing story from a stage IV deadly disease

I need a book cover design for the French translation of the US book http://www.brelvantbooks.example/Linders-Journey-Through-Illness-Story/dp/0412298765/ref=sr_1_4?s=books&ie=UTF8&qid=1455100794&sr=1-4&keywords=tam+vesko
.
I do not want the word AIDS on the French cover, as the story of this book applies to any disease.

The french title will be something like :
Un matin nouveau !
Condamné par la médecine, il guérit grâce au jeûne, la détoxination, et l’amour.

which means something like
A new morning!
Subtitle : Given up by official medecine, he managed to heal with fasting, detox and love.

Many thanks !

Target Market(s)

Anybody interested in natural health

Requirements
Must have
• Nothing special
Nice to have
• Nothing special
Should not have
• Nothing special

```html
<!DOCTYPE html>
<html lang="fr">
<head>
<meta charset="utf-8">
<title>Un matin nouveau ! — couverture</title>
<link rel="stylesheet" href="https://fonts.googleapis.com/css2?family=Bebas+Neue&family=EB+Garamond:wght@600&family=Oswald:wght@400&family=Archivo:wght@700&display=swap">
<style>
  :root {
    --ink-bg: #0d0f12;
    --paper: #ffffff;
    --accent-red: #e3161c;
    --rule-red: #5e1b1d;
    --fold-grey: #8a8d92;
  }
  * { box-sizing: border-box; margin: 0; padding: 0; }
  html, body { width: 1200px; height: 830px; overflow: hidden; background: var(--ink-bg); }
  .cover {
    position: relative;
    width: 1200px;
    height: 830px;
    background: var(--ink-bg);
    color: var(--paper);
  }

  /* Back cover */
  .back-blurb {
    position: absolute;
    left: 63px;
    top: 104px;
    width: 424px;
    font-family: "EB Garamond", Georgia, serif;
    font-weight: 600;
    font-size: 17.6px;
    line-height: 23.2px;
    text-align: justify;
    letter-spacing: 0.3px;
  }
  .back-blurb p { text-indent: 29px; }
  .back-blurb p.lead { text-indent: 0; }
  .drop-cap {
    float: left;
    font-family: "Bebas Neue", "Oswald", sans-serif;
    font-size: 94px;
    line-height: 70px;
    margin: 6px 6px 0 0;
  }

  /* Spine */
  .fold-line {
    position: absolute;
    top: 0;
    height: 830px;
    border-left: 1px dashed var(--fold-grey);
    opacity: 0.7;
  }
  .fold-line.left { left: 554px; }
  .fold-line.right { left: 647px; }
  .spine-title, .spine-author {
    position: absolute;
    writing-mode: vertical-rl;
    font-family: "Oswald", "Arial Narrow", sans-serif;
    font-weight: 400;
    color: var(--paper);
    line-height: 1;
  }
  .spine-title { left: 578px; top: 140px; font-size: 48px; }
  .spine-author { left: 586px; top: 690px; font-size: 30px; }

  /* Front cover */
  .front-title {
    position: absolute;
    left: 710px;
    top: 48px;
    font-family: "Bebas Neue", "Oswald", sans-serif;
    font-weight: 400;
    font-size: 150px;
    line-height: 140px;
    letter-spacing: 1px;
    color: var(--paper);
  }
  .rule {
    position: absolute;
    left: 684px;
    width: 486px;
    border-top: 2px dotted var(--rule-red);
  }
  .rule.top { top: 352px; }
  .rule.bottom { top: 609px; }
  .subtitle {
    position: absolute;
    left: 718px;
    top: 384px;
    font-family: "Archivo", Arial, sans-serif;
    font-weight: 700;
    font-size: 25px;
    line-height: 51px;
    letter-spacing: 1.6px;
    color: var(--accent-red);
  }
  .front-author {
    position: absolute;
    left: 716px;
    top: 706px;
    font-family: "Bebas Neue", "Oswald", sans-serif;
    font-size: 74px;
    line-height: 1;
    letter-spacing: 1px;
    color: var(--paper);
  }
</style>
</head>
<body>
<main class="cover">
  <section class="back-cover">
    <div class="back-blurb">
      <p class="lead"><span class="drop-cap">S</span>nsequia id et, culluptat quae nonsequi om molupta voloria tiorro il inctus, si occumque imusdae pedipis etur, sed minvenima ius, sitatio vel ibusae rate et mnis adis ex et dolorep ror rovidia do lores veles rerunda doleserum qui consect empedior magni voluptatium.</p>
      <p>Et omnient urenime omnis volorerci di amendae et ut aut hit, quaepellis doluptas molore latiuntoria sin nimei ncimilicid utessit, non porit eat as et inum iuscipsam inume velenec usamet viducit mintotam facesequidi cusam, corehent.</p>
      <p>Et quuntotae ex eturit aborerero id quaspit pra quodi autem hilit aut labo. Arum que eiur? Qui om nime volor simi, qui dipsum in. cilitis eaqui omnis antum illest vel iusdaes equidit et volorem et eaquis volorae re voluptam sum quibus, odio. quo bear cime eum ex earunt.</p>
      <p>Mendeni volum, odis repel ea quam voluptatum sitaeces dolupit labo. Nam alitatus.</p>
      <p>Omnihil etur amus, ut aut eiunt, inventio omnis est reruptur?</p>
      <p>Modis exerum remperrum nulpa corerep eruptat.</p>
    </div>
  </section>

  <section class="spine">
    <div class="fold-line left"></div>
    <div class="fold-line right"></div>
    <div class="spine-title">Un matin nouveau !</div>
    <div class="spine-author">Vesko</div>
  </section>

  <section class="front-cover">
    <h1 class="front-title">UN MATIN<br>NOUVEAU !</h1>
    <div class="rule top"></div>
    <p class="subtitle">Condamné par la médecine,<br>il guérit grâce au jeûne,<br>la détoxination,<br>et l’amour.</p>
    <div class="rule bottom"></div>
    <p class="front-author">TAM VESKO</p>
  </section>
</main>
</body>
</html>
```